Life Coach for Lawyers Business Card Design

Elegant, original, business card design for life coaching service for associate attorneys who work in big law and struggle with stress, overwhelm, and time management. Double sided design.

Target Market(s)

Women associate attorneys who work in big law and struggle with stress, overwhelm, and time management.

Industry/Entity Type

Life Coaching

Contact Information for Business Card

Marissa Pendrell
Life Coach
518.677.3941
calmbriefcounsel.net
marissa@calmbriefcounsel.net
@calmbriefcounsel (Instagram)

Font styles to use
Other font styles liked:
• Silver South font duo. See uploaded files.

Requirements
Must have
• Icons for phone, website, email, and Instagram instead of words. Specific colors used in my logo (171B2B, 421121, FFFFFF)
Nice to have
• Foil. Embossed. Feminine design.
Should not have
• Any colors other than those used in logo. See uploaded files.

```html
<!DOCTYPE html>
<html lang="en">
<head>
<meta charset="utf-8">
<title>Calm Brief Counsel — Business Card</title>
<link rel="stylesheet" href="https://fonts.googleapis.com/css2?family=Cinzel:wght@700&family=Lato:wght@400&family=Playfair+Display:wght@500&display=swap">
<style>
  :root {
    --navy: #171B2B;
    --wine: #421121;
    --paper: #FFFFFF;
    --backdrop: #e6e4e5;
  }
  html, body {
    margin: 0;
    padding: 0;
    width: 1200px;
    height: 896px;
    overflow: hidden;
    background: var(--backdrop);
  }
  .sheet {
    width: 1200px;
    height: 896px;
    display: flex;
    flex-direction: column;
    align-items: center;
    justify-content: center;
    gap: 30px;
  }
  .card {
    position: relative;
    width: 720px;
    height: 411px;
    background: var(--paper);
    border-bottom: 6px solid var(--wine);
    box-sizing: border-box;
    box-shadow: 0 6px 18px rgba(23, 27, 43, 0.18);
  }
  .brand-name {
    font-family: "Playfair Display", Georgia, serif;
    font-weight: 500;
    color: var(--wine);
    text-transform: uppercase;
    letter-spacing: 0.06em;
    line-height: 1.05;
    text-align: center;
    margin: 0;
  }
  /* Front */
  .card-front .contact {
    position: absolute;
    left: 48px;
    top: 128px;
  }
  .holder-name {
    font-family: "Cinzel", "Times New Roman", serif;
    font-weight: 700;
    font-size: 25px;
    letter-spacing: 0.03em;
    color: var(--wine);
    margin: 0;
  }
  .holder-role {
    font-family: "Lato", Arial, sans-serif;
    font-size: 17px;
    color: var(--navy);
    margin: 2px 0 22px;
  }
  .contact-list {
    list-style: none;
    margin: 0;
    padding: 0;
    font-family: "Lato", Arial, sans-serif;
    font-size: 17px;
    color: var(--navy);
  }
  .contact-list li {
    display: flex;
    align-items: center;
    gap: 10px;
    margin-bottom: 7px;
  }
  .contact-list svg {
    width: 13px;
    height: 13px;
    fill: var(--wine);
    flex: none;
  }
  .card-front .brand-name {
    position: absolute;
    right: 48px;
    top: 150px;
    font-size: 34px;
    width: 280px;
  }
  /* Back */
  .card-back {
    display: flex;
    align-items: center;
    justify-content: center;
  }
  .card-back .brand-name {
    font-size: 54px;
  }
</style>
</head>
<body>
<main class="sheet">
  <section class="card card-front" aria-label="Card front">
    <div class="contact">
      <h1 class="holder-name">Marissa Pendrell</h1>
      <p class="holder-role">Life Coach</p>
      <ul class="contact-list">
        <li>
          <svg viewBox="0 0 16 16" aria-hidden="true"><path d="M3.6 1.2l2.3 2.6c.3.4.3.9 0 1.3L4.8 6.3c.8 1.9 2.9 4 4.9 4.9l1.2-1.1c.4-.3.9-.3 1.3 0l2.6 2.3c.4.4.4 1 0 1.4l-1.2 1.2c-.6.6-1.5.8-2.3.5C6.7 14 2 9.3.5 4.7.2 3.9.4 3 1 2.4L2.2 1.2c.4-.4 1-.4 1.4 0z"/></svg>
          <span>518.677.3941</span>
        </li>
        <li>
          <svg viewBox="0 0 16 16" aria-hidden="true"><path d="M1 3h14v1.2L8 8.6 1 4.2z"/><path d="M1 5.6l7 4.4 7-4.4V13H1z"/></svg>
          <span>marissa@calmbriefcounsel.net</span>
        </li>
        <li>
          <svg viewBox="0 0 16 16" aria-hidden="true"><circle cx="8" cy="8" r="7"/><path d="M1 8h14M8 1c-2.4 2-2.4 12 0 14M8 1c2.4 2 2.4 12 0 14" stroke="#fff" stroke-width="1" fill="none"/></svg>
          <span>www.calmbriefcounsel.net</span>
        </li>
      </ul>
    </div>
    <p class="brand-name">Calm Brief<br>Counsel</p>
  </section>

  <section class="card card-back" aria-label="Card back">
    <p class="brand-name">Calm Brief<br>Counsel</p>
  </section>
</main>
</body>
</html>
```